Business Card Design

Certified Canine Therapeutic Massage Practitioner
Specializing in Senior Canine Massage Therapy and Giant Breeds
Certified in Canine Emergency CPR, First Aid 7 Care

Target Market(s)

Dog lovers with disposable income.

Industry/Entity Type

Business

Contact Information for Business Card

Paws At Ease Studio
415.382.6071
Brookhaven, KY
Tova@Pawsateasestudio.com

```html
<!DOCTYPE html>
<html lang="en">
<head>
<meta charset="utf-8">
<title>Paws At Ease Studio – Business Card</title>
<link rel="stylesheet" href="https://fonts.googleapis.com/css2?family=Federo&family=Archivo+Narrow:wght@500&family=Tinos:wght@400;700&display=swap">
<style>
  :root {
    --page: #ffffff;
    --card: #efedf0;
    --brand-green: #2a9a06;
    --frame-green: #2f9a12;
    --ink-dark: #111111;
    --ink-grey: #7c8888;
    --ink-light: #a2a6ab;
    --band-text: #ffffff;
  }
  html, body {
    margin: 0;
    padding: 0;
    width: 1200px;
    height: 702px;
    overflow: hidden;
    background: var(--page);
  }
  .canvas {
    position: relative;
    width: 1200px;
    height: 702px;
  }
  .card {
    position: absolute;
    left: 57px;
    top: 59px;
    width: 1082px;
    height: 586px;
    background: var(--card);
  }
  .brand-name {
    position: absolute;
    left: 97px;
    top: 76px;
    margin: 0;
    font-family: "Federo", "Marcellus", serif;
    font-weight: 400;
    font-size: 50px;
    line-height: 50px;
    color: var(--brand-green);
  }
  .brand-name .line-one { display: block; letter-spacing: 4px; }
  .brand-name .line-two { display: block; letter-spacing: 1px; }
  .portrait {
    position: absolute;
    left: 865px;
    top: 70px;
  }
  .person-name {
    position: absolute;
    left: 340px;
    top: 290px;
    margin: 0;
    font-family: "Archivo Narrow", "Arial Narrow", sans-serif;
    font-weight: 500;
    font-size: 33px;
    letter-spacing: 5px;
    color: var(--ink-dark);
  }
  .credentials {
    position: absolute;
    left: 340px;
    top: 334px;
    margin: 0;
    padding: 0;
    list-style: none;
    font-family: "Tinos", "Times New Roman", serif;
    font-size: 17px;
    line-height: 22.5px;
    letter-spacing: 0.3px;
    color: var(--ink-grey);
  }
  .phone-line {
    position: absolute;
    left: 240px;
    top: 484px;
    margin: 0;
    font-family: "Tinos", "Times New Roman", serif;
    font-size: 21px;
    letter-spacing: 3.8px;
    color: var(--ink-light);
    white-space: pre;
  }
  .contact-band {
    position: absolute;
    left: 61px;
    top: 519px;
    width: 1080px;
    height: 126px;
    background: var(--brand-green);
  }
  .online, .office {
    position: absolute;
    margin: 0;
    padding: 0;
    list-style: none;
    font-family: "Tinos", "Times New Roman", serif;
    font-size: 21px;
    color: var(--band-text);
  }
  .online { left: 33px; top: 13px; line-height: 47px; letter-spacing: 2.4px; }
  .office { left: 800px; top: 12px; line-height: 32px; font-weight: 700; letter-spacing: 1.6px; }
</style>
</head>
<body>
<div class="canvas">
  <div class="card"></div>

  <h1 class="brand-name">
    <span class="line-one">Paws At Ease</span>
    <span class="line-two">Studio</span>
  </h1>

  <svg class="portrait" width="256" height="304" viewBox="0 0 256 304" role="img" aria-label="Photo of the massage practitioner with a large dog in a garden">
    <defs>
      <linearGradient id="garden-tones" x1="0" y1="0" x2="1" y2="1">
        <stop offset="0" stop-color="#4f7a3a"/>
        <stop offset="0.45" stop-color="#c9dbe0"/>
        <stop offset="0.75" stop-color="#e8e2dc"/>
        <stop offset="1" stop-color="#5e8f3c"/>
      </linearGradient>
    </defs>
    <ellipse cx="128" cy="152" rx="121" ry="146" fill="var(--frame-green)"/>
    <ellipse cx="128" cy="152" rx="111" ry="136" fill="url(#garden-tones)"/>
  </svg>

  <h2 class="person-name">Your Name Here</h2>
  <ul class="credentials">
    <li>Certified Canine Therapeutic Massage Practitioner</li>
    <li>Specializing in Senior Canine Massage Therapy and Giant Breeds</li>
    <li>Certified in Canine Emergency CPR, First Aid 7 Care</li>
  </ul>

  <p class="phone-line">Call 123 134567898 , 123 134567898   Fax 123 00000001</p>

  <div class="contact-band">
    <ul class="online">
      <li>Web : www.pawsateasestudio.com</li>
      <li>Email :Tova@Pawsateasestudio.com</li>
    </ul>
    <ul class="office">
      <li>Paws At Ease Studio</li>
      <li>415.382.6071</li>
      <li>Brookhaven, KY</li>
    </ul>
  </div>
</div>
</body>
</html>
```